Safety Training company business card design

We are after a high quality, professional business card. We are open to a single or double sided card.

The winning designer must provide the card in a format where we can easily change the name and details of the different people in our organization.

Harbor Guard's company colour is lime green.

We provide all aspects of safety advisory and training for the Building, Civil Construction, Mining, Oil and Gas, Manufacturing, Rail, Rural and Retail sectors.

Visit our website www.harborguard.com.au for training competencies we offer along with our other services including RPL's, safety audits, professional development and client support.

Target Market(s)

Those in the Building, Civil Construction, Mining, Oil and Gas, Manufacturing, Rail, Rural and Retail industries.

Industry/Entity Type

Training

Contact Information for Business Card

Harbor Guard
Safety and Training
Dennis Palworth
Director
M 0427 518 266
dennis@harborguard.com.au
www.harborguard.com.au
(2 business addresses:)
Corvin High Risk Training Centre
17 Tandem Parade, Keswick Q 4312 P 3912 5486 F 3912 5174
Brenlow Training Centre
86 Fenwick Street, Dunmore Q 4681 P 4873 2615 F 4873 2249

Colors
9bcb3c

Requirements
Must have
• Lime green must be the main colour. must include HG logo attached, and state Harbor Guard (Safety and Training in smaller/different font).

State something along the lines of:

Nice to have
• We offer remote training and we can come to you.

```html
<!DOCTYPE html>
<html lang="en">
<head>
<meta charset="utf-8">
<title>Harbor Guard – Business Card</title>
<link href="https://fonts.googleapis.com/css2?family=Open+Sans:ital,wght@0,400;0,600;0,700;1,700&display=swap" rel="stylesheet">
<style>
  :root {
    --lime: #93bd2c;
    --stone: #9a8f8a;
    --mist: #dddddc;
    --signal-red: #e0262b;
    --ink: #2f2f2f;
    --white: #ffffff;
    --sun: #f2e21a;
  }
  * { margin: 0; padding: 0; box-sizing: border-box; }
  html, body {
    width: 1200px; height: 1037px; overflow: hidden;
    background: var(--white);
    font-family: "Open Sans", Arial, sans-serif;
    color: var(--ink);
  }
  .canvas { position: relative; width: 1200px; height: 1037px; }
  .card {
    position: absolute; width: 460px; height: 776px;
    border-radius: 32px; overflow: hidden;
    background: var(--mist);
    box-shadow: 0 4px 18px rgba(0,0,0,0.22);
  }
  .card--back { left: 80px; top: 127px; }
  .card--front { left: 637px; top: 130px; }
  .band { position: absolute; left: 0; width: 100%; }

  /* back side */
  .tagline-band { top: 0; height: 233px; background: var(--lime); }
  .tagline {
    position: absolute; top: 38px; width: 100%; text-align: center;
    font-style: italic; font-weight: 700; font-size: 21.5px; line-height: 36px;
    color: var(--ink);
  }
  .divider-band { top: 233px; height: 16px; background: var(--stone); }
  .footer-band {
    bottom: 0; height: 104px; background: var(--stone);
    display: flex; align-items: center; justify-content: center;
    color: var(--white); font-weight: 700; font-size: 23px;
  }
  .centre { position: absolute; font-size: 20px; line-height: 27px; color: #3a3a3a; }
  .centre h3 { font-size: 20px; font-weight: 700; color: var(--signal-red); margin-bottom: 10px; }
  .centre .contacts { margin-top: 12px; }
  .contact-line { display: flex; align-items: center; gap: 14px; }
  .contact-line svg { width: 18px; height: 18px; fill: var(--signal-red); flex: none; }
  .centre--corvin { left: 51px; top: 268px; }
  .centre--brenlow { right: 42px; top: 469px; text-align: right; }
  .centre--brenlow .contact-line { justify-content: flex-end; gap: 8px; }
  .mini-mark {
    position: absolute; left: 30px; top: 558px;
    display: flex; align-items: center; gap: 8px;
    font-weight: 700; font-size: 17px; color: var(--signal-red);
  }
  .mini-mark .dot { width: 22px; height: 22px; border-radius: 50%; background: var(--signal-red); }

  /* front side */
  .mark-band { top: 0; height: 236px; background: var(--stone); }
  .mark-circle {
    position: absolute; left: 166px; top: 72px;
    width: 130px; height: 130px; border-radius: 50%; background: var(--sun);
  }
  .name-band { top: 236px; height: 123px; background: var(--lime); text-align: center; }
  .brand-name {
    margin-top: 10px; font-weight: 700; font-size: 49px; letter-spacing: 1px;
    line-height: 64px; color: var(--sun); text-transform: uppercase;
  }
  .brand-sub {
    margin-top: 0; font-size: 16px; letter-spacing: 10px; color: var(--white);
    text-transform: uppercase; padding-left: 10px;
  }
  .person { position: absolute; left: 82px; top: 433px; }
  .person-name { font-size: 21px; font-weight: 700; }
  .person-role { font-size: 21px; margin-top: 6px; color: #3a3a3a; }
  .person .contacts { margin-top: 28px; font-size: 20px; color: #3a3a3a; line-height: 36px; }
  .person .contact-line { gap: 10px; }
  .person .contact-line svg { width: 20px; height: 20px; }
  .footer-band--front { height: 102px; }
</style>
</head>
<body>
<main class="canvas">

  <section class="card card--back" aria-label="Card back – locations">
    <div class="band tagline-band">
      <p class="tagline">We provide all aspects<br>of safety advisory and training<br>for Building, Civil Construction, Mining,<br>Oil and Gas, Manufacturing,<br>Rail, Rural and Retail sectors</p>
    </div>
    <div class="band divider-band"></div>

    <div class="centre centre--corvin">
      <h3>Corvin High Risk Training Centre</h3>
      <p>17 Tandem Parade,<br>Keswick Q 4312</p>
      <div class="contacts">
        <p class="contact-line"><svg viewBox="0 0 24 24"><path d="M6.6 10.8a15 15 0 0 0 6.6 6.6l2.2-2.2c.3-.3.7-.4 1-.2 1.1.4 2.3.6 3.6.6.6 0 1 .4 1 1V20c0 .6-.4 1-1 1A17 17 0 0 1 3 4c0-.6.4-1 1-1h3.5c.6 0 1 .4 1 1 0 1.3.2 2.5.6 3.6.1.3 0 .7-.2 1z"/></svg>07 3912 5486</p>
        <p class="contact-line"><svg viewBox="0 0 24 24"><path d="M6 2h9l3 3v5H6zM3 11h18v10H3zm3 3v2h4v-2zm8 0v2h2v-2zm-8 3v2h4v-2zm8 0v2h2v-2z"/></svg>07 3912 5174</p>
      </div>
    </div>

    <div class="mini-mark"><span class="dot"></span>Harbor Guard</div>

    <div class="centre centre--brenlow">
      <h3>Brenlow Training Centre</h3>
      <p>86 Fenwick Street,<br>Dunmore Q 4681</p>
      <div class="contacts">
        <p class="contact-line"><svg viewBox="0 0 24 24"><path d="M6.6 10.8a15 15 0 0 0 6.6 6.6l2.2-2.2c.3-.3.7-.4 1-.2 1.1.4 2.3.6 3.6.6.6 0 1 .4 1 1V20c0 .6-.4 1-1 1A17 17 0 0 1 3 4c0-.6.4-1 1-1h3.5c.6 0 1 .4 1 1 0 1.3.2 2.5.6 3.6.1.3 0 .7-.2 1z"/></svg>07 4873 2615</p>
        <p class="contact-line"><svg viewBox="0 0 24 24"><path d="M6 2h9l3 3v5H6zM3 11h18v10H3zm3 3v2h4v-2zm8 0v2h2v-2zm-8 3v2h4v-2zm8 0v2h2v-2z"/></svg>07 4873 2249</p>
      </div>
    </div>

    <div class="band footer-band">www.harborguard.com.au</div>
  </section>

  <section class="card card--front" aria-label="Card front – contact">
    <div class="band mark-band"><span class="mark-circle"></span></div>
    <div class="band name-band">
      <p class="brand-name">Harbor Guard</p>
      <p class="brand-sub">Safety and Training</p>
    </div>

    <div class="person">
      <p class="person-name">Dennis Palworth</p>
      <p class="person-role">Director</p>
      <div class="contacts">
        <p class="contact-line"><svg viewBox="0 0 24 24"><path d="M7 1h10a2 2 0 0 1 2 2v18a2 2 0 0 1-2 2H7a2 2 0 0 1-2-2V3a2 2 0 0 1 2-2zm0 3v14h10V4zm4 15.5v1.5h2v-1.5z" fill="var(--signal-red)"/></svg>0427 518 266</p>
        <p class="contact-line"><svg viewBox="0 0 24 24"><path d="M2 5h20v14H2zm2 2v.4l8 5.6 8-5.6V7zm0 2.8V17h16V9.8l-8 5.6z"/></svg>dennis@harborguard.com.au</p>
      </div>
    </div>

    <div class="band footer-band footer-band--front">www.harborguard.com.au</div>
  </section>

</main>
</body>
</html>
```